3D Buchcover für ebook
Das Design kam überraschend und war quasi aus dem Stand perfekt. Ich konnte gar nicht anders, als es zum Gewinner zu küren.
Zielgruppe
Das Buch erscheint als ebook, später auch als gedruckte Version. Es spricht Personen an, die mittels einer Diät nicht nur ihre Figur, sondern auch ihre Gesundheit, Fitneß und das Aussehen im Allgemeinen verbessern wollen. Die Hauptzielgruppe sind Frauen zwischen 35 und 60+.
Branche: Medizin/Gesundheit.
Aufgabenstellung
Hergestellt werde soll das Cover für ein ebook mit dem Titel "Der schmale Gürtel als klarer Beweis". Außerdem soll folgende Headline untegebracht werden: "Rückblick auf 13 Jahre Alltag ohne Zucker". Es soll ein Bild der Autorin verwendet werden. Aus den gelieferten Vorlagen kann die Frauenfigur ausgeschnitten werden. Wichtig ist, ihre Figur und die Ausstrahlung wirkungsvoll zur Geltung zu bringen. Unter den mitgelieferten Deteien ist außerdem das aktuelle Cover enthalten (das Buch ist bereits veröffentlicht). Auch der Autorname "Hanna Lübeck" soll auf dem Cover Platz finden.
Das Cover soll auch im Kleinformat, wie es üblicherweise in den Suchergebnissen auf Veltrix angezeigt wird, eine Aussagekraft besitzen.

```html
<!DOCTYPE html>
<html lang="de">
<head>
<meta charset="utf-8">
<title>Der schmale Gürtel als klarer Beweis – Hanna Lübeck</title>
<link rel="stylesheet" href="https://fonts.googleapis.com/css2?family=Bebas+Neue&family=Roboto+Condensed:wght@700&display=swap">
<style>
  :root {
    --denim-light: #9fb6cc;
    --denim-mid: #7390ad;
    --denim-dark: #4d6a8a;
    --hole-navy: #1c2738;
    --fray: #e9ecef;
    --accent-red: #e2231a;
    --band-white: #ffffff;
    --stitch-grey: #9a9a9a;
    --ink: #1a1a1a;
    --paper: #ffffff;
  }
  * { margin: 0; padding: 0; box-sizing: border-box; }
  html, body { width: 849px; height: 1200px; overflow: hidden; background: var(--paper); }
  .cover {
    position: relative;
    width: 849px;
    height: 1200px;
    overflow: hidden;
    font-family: "Roboto Condensed", "Arial Narrow", sans-serif;
  }
  .denim-backdrop {
    position: absolute; inset: 0;
    background: radial-gradient(ellipse at 35% 40%, var(--denim-light) 0%, var(--denim-mid) 55%, var(--denim-dark) 100%);
  }
  .torn-hole { position: absolute; left: 0; top: 0; }
  .author-portrait {
    position: absolute;
    left: 548px; top: 58px;
    width: 301px; height: 1142px;
    background: linear-gradient(180deg, #b07850 0%, #d9a88a 18%, #222 34%, #1d2b4a 70%, #1b2644 100%);
    border-radius: 140px 0 0 0;
  }
  .author-label {
    position: absolute;
    left: 0; top: 0;
    width: 312px; height: 74px;
    background: var(--accent-red);
    border-bottom: 3px dashed rgba(255,255,255,.55);
    display: flex; align-items: center; justify-content: center;
    color: var(--band-white);
    font-size: 33px;
    letter-spacing: .5px;
  }
  .title {
    position: absolute;
    right: 380px;
    top: 262px;
    text-align: right;
    font-family: "Bebas Neue", "Oswald", sans-serif;
    color: var(--fray);
    line-height: .86;
  }
  .title span { display: block; }
  .title__lead { font-size: 104px; }
  .title__key { font-size: 150px; }
  .title__tail { font-size: 66px; line-height: 1.02; }
  .subtitle-band {
    position: absolute;
    left: 0; top: 917px;
    width: 849px; height: 161px;
    background: var(--band-white);
  }
  .subtitle-band::before, .subtitle-band::after {
    content: ""; position: absolute; left: 0; right: 0;
    border-top: 3px dashed var(--stitch-grey);
  }
  .subtitle-band::before { top: 9px; }
  .subtitle-band::after { bottom: 9px; }
  .subtitle {
    position: absolute; top: 0; height: 100%;
    display: flex; align-items: center;
    color: var(--ink);
    font-size: 34px;
  }
  .subtitle--left { left: 28px; width: 290px; justify-content: flex-end; }
  .subtitle--right { left: 492px; }
  .lens { position: absolute; left: 0; top: 0; }
  .lens-text {
    position: absolute;
    left: 326px; top: 923px;
    width: 156px;
    text-align: center;
    color: var(--accent-red);
  }
  .lens-text__number { display: block; font-size: 62px; line-height: 1; }
  .lens-text__unit { display: block; font-size: 36px; line-height: 1; margin-top: 6px; }
</style>
</head>
<body>
<main class="cover">
  <div class="denim-backdrop" role="img" aria-label="Hellblauer Jeansstoff als Hintergrund"></div>

  <svg class="torn-hole" width="849" height="1200" viewBox="0 0 849 1200" aria-hidden="true">
    <path d="M150 200 C260 170 420 180 540 215 C575 300 565 420 560 520 C556 610 560 680 540 735 C420 745 300 735 190 720 C140 640 120 520 112 420 C106 330 118 250 150 200 Z"
          fill="var(--fray)" opacity=".85"/>
    <path d="M165 218 C270 192 410 200 520 232 C548 310 542 420 538 515 C535 600 538 665 522 715 C410 722 300 714 205 700 C160 625 143 520 136 420 C131 335 142 262 165 218 Z"
          fill="var(--hole-navy)"/>
  </svg>

  <div class="author-portrait" role="img" aria-label="Freigestelltes Foto der Autorin in schwarzem Top und enger Jeans"></div>

  <div class="author-label">Hanna Lübeck</div>

  <h1 class="title">
    <span class="title__lead">Der schmale</span>
    <span class="title__key">Gürtel</span>
    <span class="title__tail">als klarer</span>
    <span class="title__tail">Beweis</span>
  </h1>

  <div class="subtitle-band">
    <p class="subtitle subtitle--left">Rückblick auf</p>
    <p class="subtitle subtitle--right">Alltag ohne Zucker</p>
  </div>

  <svg class="lens" width="849" height="1200" viewBox="0 0 849 1200" aria-hidden="true">
    <line x1="378" y1="1070" x2="352" y2="1190" stroke="var(--accent-red)" stroke-width="14" stroke-linecap="round"/>
    <circle cx="404" cy="993" r="80" fill="var(--band-white)" stroke="var(--accent-red)" stroke-width="12"/>
  </svg>
  <p class="lens-text">
    <span class="lens-text__number">13</span>
    <span class="lens-text__unit">Jahre</span>
  </p>
</main>
</body>
</html>
```